【サイトマップ】
①TOP
②会社概要
③初めての方へ
④施工の流れ
⑤費用一覧
⑥外壁塗装
⑦屋根塗装
⑧内装塗装
⑨塗料紹介
⑩防水工事
⑪よくある質問
⑫施工事例(一覧)
⑬施工事例(詳細)
⑭お知らせ(一覧)
⑮お知らせ(詳細)
⑯ブログ(一覧)
⑰ブログ(詳細)
⑱お問合せ

■デザインのテイスト
・清潔な
・やさしい
・親しみやすい
・ナチュラルな

■希望デザインカラー
茶系(自然・モダン・高級感)
緑系(健康・ナチュラル)

■参考サイト
<デザイン参考>
https://www.example-hanabi-toso.com/
やさしい雰囲気があり、このサイトが一番イメージに近いです
https://www.example-verde-kanou.jp/
https://example-yamabukikensetsukogyo.co.jp/

<使用カラー参考>
https://example-kaze-reform.jp/
https://example-ueno-dental.net/
https://example-kpv.jp/
https://example-suzuha.jp/hotel/
https://www.example-kirino.co.jp/40th/ie/meadow/little_wrens.html
http://www.example-lemontea.co.jp/

■フォントについて
・無料で使えるwebフォントで作成お願い致します
・OSに紐づくフォントの使用は控えていただければと思います (ヒラギノなど)

■文章について
・現行ホームページに記載しているテキストを使用して下さい。
・可能な限り「ダミーテキスト」を繰り返した文字の配置は避けてください。

■制作要望・素材・ロゴ・サイトマップについて
・下記よりダウンロードしてご使用ください
URL:https://example-fileport.jp/download/a1b2c3d4e5f60718293a4b5c6d7e8f9012345678
パスワード:k7214mzxp5

■写真について
・Pictora Bank( https://bank.example-pictora.com/jp/ )で定期契約をしています
また定期契約のものは弊社の負担となり、ランサー様に負担はありません。
・カンプ画像を入れてください
その際、通常アセットで購入できる画像でお願いいたします。

■その他
・業務への支障がでる可能性がございますので、店舗への直接の連絡はお控え下さい
・申し訳ございませんがXD形式の納品はお受けできかねます。
・デザインの横幅は1300pxで作成お願いいたします。
より多くのデザイン案を拝見したいため、期日の延長を行います。
皆様よろしくお願いいたします。
ワイヤーフレームを添付いたします。
よろしければ参照しながらデザインをお願いいたします。

必ずこの配置にしなければならないわけではございませんので
ご提案がございましたら、そちらもお待ちしております。

何卒宜しくお願いいたします。
https://view.example-wireboard.com/view/9c8e7a6b-1d2f-4e3a-8b7c-6a5d4e3f2b1a-3ce2/
再度延長を行います。

シンプルなものの、イラストなどを用いた柔らかさ・ポップさに気に入りました。

修正にも迅速にご対応いただきましてありがとうございました。

```html
<!DOCTYPE html>
<html lang="ja">
<head>
<meta charset="utf-8">
<title>有限会社花森美装</title>
<link href="https://fonts.googleapis.com/css2?family=Zen+Maru+Gothic:wght@400;500;700;900&display=swap" rel="stylesheet">
<style>
:root{
  --green:#5fa52a;
  --green-dark:#3f7f1c;
  --green-light:#e6efd6;
  --green-pale:#f1f6e8;
  --lime:#cfe08a;
  --beige:#f6f2ea;
  --brown:#5b4633;
  --text:#2b2b2b;
  --muted:#555;
  --white:#fff;
}
*{margin:0;padding:0;box-sizing:border-box}
html,body{width:1200px;height:5068px;overflow:hidden}
body{font-family:"Zen Maru Gothic",sans-serif;color:var(--text);background:var(--white);position:relative}
.abs{position:absolute}
.photo{position:absolute}

/* header */
.site-header{position:absolute;left:0;top:0;width:1200px;height:100px;background:var(--white);z-index:2}
.logo{position:absolute;left:40px;top:18px;font-size:26px;font-weight:900;color:var(--green-dark);letter-spacing:1px}
.tel{position:absolute;left:760px;top:20px;font-size:28px;font-weight:900;color:var(--text)}
.tel small{font-size:14px;margin-right:8px}
.btn-contact{position:absolute;left:990px;top:18px;width:170px;height:40px;background:var(--green);color:#fff;font-size:15px;font-weight:700;border-radius:4px;display:flex;align-items:center;justify-content:center;gap:8px}
.gnav{position:absolute;left:40px;top:68px;display:flex;gap:44px;font-size:14px;font-weight:700}
.gnav span::after{content:"";display:inline-block}

/* hero */
.hero{left:0;top:100px;width:1200px;height:372px;background:linear-gradient(100deg,#c9cfc6 0%,#9fae98 35%,#7f9a72 60%,#a8b99c 100%)}
.hero-copy{position:absolute;left:560px;top:250px;color:#fff;font-size:44px;font-weight:900;line-height:1.5;letter-spacing:4px;text-shadow:0 2px 6px rgba(0,0,0,.35)}
.news-bar{position:absolute;left:0;top:472px;width:1200px;height:44px;background:var(--brown);color:#fff;display:flex;align-items:center;font-size:14px}
.news-bar .label{margin-left:40px;font-weight:700;width:200px}
.news-bar .date{width:160px;text-align:center}
.news-bar .more{margin-left:auto;margin-right:50px}

/* section title */
.sec-title{position:absolute;left:0;width:1200px;display:flex;align-items:center;justify-content:center;gap:24px;font-size:36px;font-weight:900}
.sec-title::before,.sec-title::after{content:"";width:80px;height:6px;background:var(--green);border-radius:3px}
.btn-green{position:absolute;height:48px;background:var(--green);color:#fff;font-size:16px;font-weight:700;display:flex;align-items:center;justify-content:center;border-radius:2px;box-shadow:4px 4px 0 var(--green-dark)}

/* works */
.works-lead{position:absolute;left:440px;top:700px;width:320px;text-align:center;font-size:20px;font-weight:900;line-height:1.7;color:var(--text)}

/* strengths */
.strength-bg{left:0;top:1200px;width:1200px;height:560px;background:var(--beige)}
.point-card{position:absolute;top:1370px;width:270px;height:350px;background:#fff;padding:24px 26px}
.point-card .icon{position:absolute;left:22px;top:-14px;width:48px;height:70px;background:#e9e4da;border-radius:8px}
.point-card .tag{position:absolute;left:100px;top:20px;width:140px;height:26px;background:var(--green);color:#fff;font-size:13px;font-weight:700;display:flex;align-items:center;padding-left:12px}
.point-card h3{position:absolute;left:0;top:78px;width:100%;text-align:center;font-size:20px;font-weight:900}
.point-card h3::after{content:"";display:block;width:200px;height:2px;background:var(--green);margin:12px auto 0}
.point-card p{position:absolute;left:26px;top:140px;width:218px;font-size:14px;line-height:2.1;color:var(--muted)}

/* greeting */
.greet-bg{left:0;top:1760px;width:1200px;height:430px;background:var(--green-light)}
.greet-title{position:absolute;left:140px;top:1830px;display:flex;align-items:center;gap:20px;font-size:34px;font-weight:900}
.greet-title::before{content:"";width:70px;height:6px;background:var(--green);border-radius:3px}
.greet-lead{position:absolute;left:140px;top:1900px;width:440px;font-size:16px;font-weight:900;line-height:1.9}
.greet-text{position:absolute;left:140px;top:1985px;width:440px;font-size:14px;line-height:2;color:var(--muted)}

/* services */
.service-bg{left:0;top:2190px;width:1200px;height:1800px;background:var(--beige)}
.svc-label{position:absolute;height:56px;width:230px;background:var(--lime);display:flex;align-items:center;justify-content:center;font-size:24px;font-weight:900;box-shadow:-8px 8px 0 var(--green)}
.svc-text{position:absolute;width:420px;font-size:14px;line-height:2;color:var(--muted)}
.svc-photo{position:absolute;border-radius:46% 54% 50% 50% / 52% 48% 52% 48%}

/* bottom banners */
.banner{position:absolute;top:4080px;width:430px;height:160px;background:#fff;border:3px solid var(--green);box-shadow:8px 8px 0 var(--green);display:flex;align-items:center}
.banner .pic{width:160px;height:110px;margin-left:22px;border-radius:6px}
.banner .txt{margin-left:30px;font-size:26px;font-weight:900}

/* blog */
.blog-card{position:absolute;top:4370px;width:270px}
.blog-card .pic{height:200px}
.blog-card .date{margin-top:12px;font-size:12px;color:var(--muted)}
.blog-card .ttl{margin-top:6px;font-size:15px;font-weight:700}

/* footer */
.footer-bg{left:0;top:4760px;width:1200px;height:308px;background:var(--green-light)}
.f-logo{position:absolute;left:140px;top:4800px;font-size:28px;font-weight:900;color:var(--green-dark)}
.f-addr{position:absolute;left:140px;top:4850px;font-size:13px;color:var(--muted)}
.f-tel{position:absolute;left:140px;top:4880px;font-size:26px;font-weight:900}
.f-tel small{font-size:13px;margin-right:8px}
.f-btn{position:absolute;left:140px;top:4935px;width:170px;height:38px;background:var(--green);color:#fff;font-size:14px;font-weight:700;display:flex;align-items:center;justify-content:center;border-radius:3px}
.f-col{position:absolute;top:4810px;font-size:13px;line-height:2;color:var(--muted)}
.f-col b{color:var(--text);display:block}
.f-col b::before{content:"■";color:var(--green);margin-right:4px}
.copyright{position:absolute;left:0;top:5032px;width:1200px;height:36px;background:var(--green);color:#fff;font-size:11px;display:flex;align-items:center;justify-content:center}
</style>
</head>
<body>

<header class="site-header">
  <div class="logo">有限会社花森美装</div>
  <div class="tel"><small>TEL.</small>000-000-0000</div>
  <div class="btn-contact">
    <svg width="18" height="14" viewBox="0 0 18 14"><rect x="1" y="1" width="16" height="12" fill="none" stroke="#fff" stroke-width="2"/><path d="M1 1l8 7 8-7" fill="none" stroke="#fff" stroke-width="2"/></svg>
    お問い合わせ</div>
  <nav class="gnav"><span>TOP</span><span>花森美装について ▾</span><span>サービス内容 ▾</span><span>施工事例</span><span>初めての方へ</span><span>よくある質問</span><span>お問い合わせ</span></nav>
</header>

<div class="photo hero" role="img" aria-label="足場の上で外壁を塗装する作業員の写真"></div>
<div class="hero-copy">お客様のお悩みに合わせて<br>　　最適な提案を</div>
<div class="news-bar"><span class="label">お知らせ</span><span class="date">2022.01.25</span><span>ホームページをリニューアルいたしました。</span><span class="more">一覧へ ›</span></div>

<!-- works -->
<h2 class="sec-title" style="top:580px">花森美装の施工事例</h2>
<div class="works-lead">外壁塗装をメインにお家の修理や<br>防水工事などマルチに対応できます！</div>
<div class="photo" role="img" aria-label="施工後の住宅外観の写真" style="left:160px;top:760px;width:220px;height:210px;background:linear-gradient(#bcd2e6,#e9e4da 60%,#7a8a6a)"></div>
<div class="photo" role="img" aria-label="施工後の住宅外観の写真" style="left:400px;top:850px;width:190px;height:170px;background:linear-gradient(#c7d9ea,#f0ede6 55%,#8b8a84)"></div>
<div class="photo" role="img" aria-label="施工後の住宅外観の写真" style="left:620px;top:850px;width:190px;height:170px;background:linear-gradient(#cfe0ee,#e4e1dc 55%,#6f7f66)"></div>
<div class="photo" role="img" aria-label="施工後の住宅外観の写真" style="left:840px;top:760px;width:210px;height:210px;background:linear-gradient(#d9e6ef,#d9c7ad 55%,#8a7458)"></div>
<div class="btn-green" style="left:470px;top:1100px;width:260px">施工事例一覧へ</div>

<!-- strengths -->
<div class="abs strength-bg"></div>
<svg class="abs" style="left:0;top:1170px" width="1200" height="40" viewBox="0 0 1200 40"><path d="M0 30 Q300 0 600 24 T1200 18 V40 H0Z" fill="#f6f2ea"/></svg>
<h2 class="sec-title" style="top:1280px">花森美装の強み</h2>
<div class="point-card" style="left:150px"><div class="icon" role="img" aria-label="塗料缶のイラスト"></div><div class="tag">POINT 01</div><h3>強みタイトル</h3><p>地域に密着し、丁寧な下地処理と確かな技術で長持ちする仕上がりをお約束します。小さなご相談にも迅速に対応いたします。</p></div>
<div class="point-card" style="left:465px"><div class="icon" role="img" aria-label="スプレー缶のイラスト"></div><div class="tag">POINT 02</div><h3>強みタイトル</h3><p>現地調査からお見積り、施工、アフター点検まで自社で一貫して担当するため、中間費用を抑えた適正価格でご提案します。</p></div>
<div class="point-card" style="left:780px"><div class="icon" role="img" aria-label="塗料ボトルのイラスト"></div><div class="tag">POINT 03</div><h3>強みタイトル</h3><p>経験豊富な職人が在籍し、外壁・屋根・防水まで幅広く対応。お住まいの状態に合わせた塗料を選びご提案いたします。</p></div>

<!-- greeting -->
<div class="abs greet-bg"></div>
<div class="photo" role="img" aria-label="ローラーを持つ作業服姿の職人の写真" style="left:600px;top:1760px;width:600px;height:430px;background:linear-gradient(120deg,#eef1f3,#c4ccd6 55%,#8a98a9)"></div>
<h2 class="greet-title">代表あいさつ</h2>
<p class="greet-lead">お住まいを守る塗装で、暮らしに安心と笑顔を。<br>一軒一軒に真心を込めて施工いたします。</p>
<p class="greet-text">創業以来、地域の皆さまに支えられてまいりました。お客様の大切なお住まいを長く美しく保つため、丁寧な説明と誠実な施工を心がけております。どんな小さなことでもお気軽にご相談ください。</p>

<!-- services -->
<div class="abs service-bg"></div>
<svg class="abs" style="left:0;top:2160px" width="1200" height="40" viewBox="0 0 1200 40"><path d="M0 20 Q300 40 600 16 T1200 24 V40 H0Z" fill="#f6f2ea"/></svg>
<h2 class="sec-title" style="top:2240px">サービス内容</h2>

<div class="svc-label" style="left:260px;top:2380px">外壁塗装</div>
<p class="svc-text" style="left:150px;top:2470px">紫外線や雨風から建物を守る外壁塗装。ひび割れや色あせを点検し、下地補修から仕上げまで丁寧に行います。お住まいの印象を一新し、建物の寿命を延ばします。</p>
<div class="photo svc-photo" role="img" aria-label="ローラーで外壁を塗装する写真" style="left:620px;top:2340px;width:440px;height:300px;background:linear-gradient(135deg,#f2f2f0,#cfd3d6 60%,#b8bcbf)"></div>

<div class="photo svc-photo" role="img" aria-label="屋根を塗装する写真" style="left:140px;top:2680px;width:440px;height:300px;background:linear-gradient(135deg,#7fb3c9,#3f7f9c 55%,#a5b3b8)"></div>
<div class="svc-label" style="left:730px;top:2760px">屋根塗装</div>
<p class="svc-text" style="left:640px;top:2850px">屋根は最も傷みやすい場所です。高圧洗浄でコケや汚れを落とし、遮熱塗料なども含め最適な塗料で塗り替えます。雨漏りの予防にもつながります。</p>

<div class="svc-label" style="left:260px;top:3060px">内装塗装</div>
<p class="svc-text" style="left:150px;top:3150px">壁や天井の汚れ、黄ばみが気になる室内も塗装で明るく生まれ変わります。においの少ない塗料を使用し、住みながらの施工にも対応いたします。</p>
<div class="photo svc-photo" role="img" aria-label="刷毛で室内を塗装する写真" style="left:620px;top:3020px;width:440px;height:300px;background:linear-gradient(135deg,#fbf6e4,#efe2b8 55%,#d8e0c8)"></div>

<div class="photo svc-photo" role="img" aria-label="防水工事の作業写真" style="left:140px;top:3340px;width:440px;height:300px;background:linear-gradient(135deg,#c7b7a5,#9d6a5a 55%,#d9d4cc)"></div>
<div class="svc-label" style="left:730px;top:3400px">防水工事</div>
<p class="svc-text" style="left:640px;top:3490px">ベランダや屋上の防水層は年月とともに劣化します。状態に合わせた工法で施工し、雨水の侵入から大切なお住まいをしっかり守ります。</p>

<!-- banners -->
<svg class="abs" style="left:0;top:3900px" width="1200" height="400" viewBox="0 0 1200 400"><path d="M0 60 Q200 10 400 50 T800 40 T1200 30 V400 H0Z" fill="#cfe08a" opacity=".55"/><path d="M0 90 Q300 40 600 80 T1200 70 V400 H0Z" fill="#e6efd6"/></svg>
<div class="banner" style="left:140px"><div class="pic" role="img" aria-label="書類と家の模型のイラスト" style="background:linear-gradient(135deg,#d9e8c2,#8cbf5a)"></div><div class="txt">初めての方へ</div></div>
<div class="banner" style="left:630px"><div class="pic" role="img" aria-label="Q&Aの積み木の写真" style="background:linear-gradient(135deg,#efe4d2,#b89b78)"></div><div class="txt">よくある質問</div></div>

<!-- blog -->
<h2 class="sec-title" style="top:4320px">ブログ</h2>
<div class="blog-card" style="left:150px"><div class="pic" role="img" aria-label="家の模型と芝生の写真" style="background:linear-gradient(#e8efe0,#7fae5a)"></div><div class="date">2022.01.10</div><div class="ttl">ブログのタイトルが入ります</div></div>
<div class="blog-card" style="left:465px"><div class="pic" role="img" aria-label="白い住宅外観の写真" style="background:linear-gradient(#cfe1f0,#eeeae2 60%,#9fa88f)"></div><div class="date">2022.01.20</div><div class="ttl">ブログのタイトルが入ります</div></div>
<div class="blog-card" style="left:780px"><div class="pic" role="img" aria-label="家の模型と植物の写真" style="background:linear-gradient(#f4f4f0,#dfe6d4 60%,#b4c79a)"></div><div class="date">2022.01.25</div><div class="ttl">ブログのタイトルが入ります</div></div>
<div class="btn-green" style="left:495px;top:4660px;width:210px">ブログ一覧へ</div>

<!-- footer -->
<div class="abs footer-bg"></div>
<svg class="abs" style="left:0;top:4735px" width="1200" height="30" viewBox="0 0 1200 30"><path d="M0 20 Q300 0 600 18 T1200 12 V30 H0Z" fill="#e6efd6"/></svg>
<div class="f-logo">有限会社花森美装</div>
<div class="f-addr">〒000-0000　架空県みどり市花森町1-2-3</div>
<div class="f-tel"><small>TEL.</small>000-000-0000</div>
<div class="f-btn">お問い合わせ</div>
<div class="f-col" style="left:600px"><b>花森美装について</b>・会社概要<br>・初めての方へ<br>・施工の流れ<br>・費用一覧<br>・施工事例<br>・よくある質問</div>
<div class="f-col" style="left:800px"><b>サービス内容</b>・外壁塗装<br>・屋根塗装<br>・内装塗装<br>・塗料紹介<br>・防水工事</div>
<div class="f-col" style="left:980px"><b>その他</b>・お知らせ<br>・ブログ<br>・お問い合わせ</div>
<div class="copyright">© 有限会社花森美装 All Rights Reserved.</div>

</body>
</html>
```